Super Design, sehr nette Konversation, Anpassungen wurden schnell verwirklicht. Bin rund um zufrieden! Gerne wieder.
Zielgruppe
Plattform für KFZ-Dienstleistungen (KFZ-Inspektion, Smart Repair, Fahrzeugaufbereitung, Innenreinigung, etc).
Haben aber im Bereich Fahrzeugpflege eigens ausgeführte Dienstleistungen.
Unsere Dienstleistungen werden während der Arbeit unseres Kunden durchgeführt. Annahmestellen (Schließfachsysteme) sind rund um die Arbeitsstätten unserer Kunden. Wir bieten für ausgewählte Orte auch einen Hol- und Bringservice.
Buchungen laufen über unseren Online-Shop unter glanzamort.de/shop
B2C-Kunden, Vorallem Kunden zwischen 25 und 55 Jahren.
Wir brauchen einen Flyer der dem Kunden unsere verschidenen Leistungen nährer bringt.
Logo in Weiß und Blau hinterlegt. Je nach Design verwenden.
Aufgabenstellung
Flyer in A6 Hochformat, gerne auch beidseitig.
Leistungen:
Reifenwechsel 39,95€ (Mit Reifenwäsche)
Smart-Repair ab 9,95€ (Kratzer und Schrammen, Dellen und Beulen)
KFZ-Inspektion ab 349,95€ (Großer Service & Kleiner Service)
Fahrzeugpflege ab 23,95€ (Innen- & Außenreinigung)
Lackaufbereitung & Politur
Website: glanzamort.de

```html
<!DOCTYPE html>
<html lang="de">
<head>
<meta charset="utf-8">
<title>KFZ-Dienstleistungen Flyer</title>
<link href="https://fonts.googleapis.com/css2?family=Saira+Semi+Condensed:wght@300;400;500;600;700&display=swap" rel="stylesheet">
<style>
  :root {
    --navy-dark: #141b3a;
    --navy-light: #1f5479;
    --slate: #4b5f86;
    --gold: #e1ab12;
    --gold-band: #e2ae0b;
    --ink: #1a2745;
    --white: #ffffff;
  }
  html, body { margin: 0; padding: 0; overflow: hidden; background: #ffffff; }
  .flyer {
    position: relative;
    width: 851px;
    height: 1200px;
    overflow: hidden;
    background: var(--white);
    font-family: "Saira Semi Condensed", "Arial Narrow", sans-serif;
  }
  .backdrop { position: absolute; inset: 0; }
  .layer { position: absolute; margin: 0; white-space: nowrap; }

  .headline {
    color: var(--white);
    font-weight: 500;
    font-size: 32px;
    line-height: 1;
    text-shadow: 1px 2px 3px rgba(0,0,0,.6);
  }

  .section-title { font-weight: 700; font-size: 24px; line-height: 1; }
  .services-title { left: 0; width: 425px; text-align: center; top: 406px; color: var(--slate); }
  .services-title .accent { color: var(--gold); }
  .steps-title { left: 430px; width: 421px; text-align: center; top: 386px; color: var(--white); }

  .service { left: 0; width: 415px; text-align: center; }
  .service .name { display: block; color: var(--slate); font-weight: 500; font-size: 22px; line-height: 29px; }
  .service .detail { display: block; color: var(--gold); font-weight: 500; font-size: 19px; line-height: 27px; }

  .step { left: 440px; width: 401px; text-align: center; color: var(--white); }
  .step .number { display: block; font-weight: 300; font-size: 44px; line-height: 44px; margin-bottom: 10px; }
  .step .text { display: block; font-weight: 300; font-size: 18px; line-height: 30px; }

  .icon-slot { position: absolute; border-radius: 6px; }

  .footer-logo {
    position: absolute; left: 44px; top: 1120px;
    display: flex; align-items: center; gap: 10px;
    color: var(--white); font-weight: 600; font-size: 28px;
  }
  .footer-logo .mark { width: 22px; height: 22px; background: var(--white); }

  .contact { position: absolute; color: var(--ink); font-weight: 600; font-size: 18px; line-height: 1; }
  .contact.address { font-size: 14px; }
</style>
</head>
<body>
<div class="flyer">
  <svg class="backdrop" width="851" height="1200" viewBox="0 0 851 1200">
    <defs>
      <linearGradient id="panel" x1="0" y1="0" x2="0" y2="1">
        <stop offset="0" stop-color="#141b3a"/>
        <stop offset="1" stop-color="#1f5479"/>
      </linearGradient>
      <linearGradient id="photo" x1="0" y1="0" x2="1" y2="1">
        <stop offset="0" stop-color="#2a261e"/>
        <stop offset=".45" stop-color="#5a4a2c"/>
        <stop offset=".75" stop-color="#3a4c78"/>
        <stop offset="1" stop-color="#1d1b18"/>
      </linearGradient>
      <linearGradient id="fade" x1="0" y1="0" x2="1" y2="0">
        <stop offset="0" stop-color="#ffffff" stop-opacity="0"/>
        <stop offset="1" stop-color="#c9ccd3" stop-opacity=".6"/>
      </linearGradient>
    </defs>
    <rect class="steps-panel" x="430" y="318" width="421" height="760" fill="url(#panel)"/>
    <rect x="412" y="395" width="18" height="683" fill="url(#fade)"/>
    <polygon class="hero-photo" role="img" aria-label="Foto: Hand im blauen Handschuh reinigt mit rotem Mikrofasertuch ein Fahrzeug-Armaturenbrett"
      points="0,0 851,0 851,405 530,340 430,320 0,272" fill="url(#photo)"/>
    <polygon class="accent-stripe" points="80,285 430,356 430,395 82,320" fill="var(--gold)"/>
    <rect class="footer-band" x="0" y="1077" width="851" height="123" fill="var(--gold-band)"/>
    <line x1="259" y1="1096" x2="259" y2="1185" stroke="#ffffff" stroke-width="5"/>

    <g fill="none" stroke="#ffffff" stroke-width="2.2">
      <rect x="283" y="1102" width="36" height="26"/>
      <polyline points="283,1102 301,1118 319,1102"/>
      <circle cx="568" cy="1116" r="13"/>
      <ellipse cx="568" cy="1116" rx="6" ry="13"/>
      <line x1="555" y1="1116" x2="581" y2="1116"/>
      <line x1="557" y1="1109" x2="579" y2="1109"/>
      <line x1="557" y1="1123" x2="579" y2="1123"/>
    </g>
    <path d="M290,1143 q-8,6 -3,20 q5,14 14,19 l4,-5 q-6,-4 -9,-12 q-3,-8 -1,-13 z" fill="#ffffff"/>
    <path d="M568,1146 a12,12 0 0 1 12,12 c0,9 -12,22 -12,22 c0,0 -12,-13 -12,-22 a12,12 0 0 1 12,-12 z" fill="#ffffff"/>
    <circle cx="568" cy="1158" r="4.5" fill="var(--gold-band)"/>
  </svg>

  <h1 class="layer headline" style="left:14px; top:208px;">Professionelle KFZ-Dienstleistungen</h1>
  <p class="layer headline" style="left:147px; top:255px;">in Ingolstadt und umgebung</p>

  <h2 class="layer section-title services-title">Unsere <span class="accent">Leistungen</span> im Überblick</h2>

  <div class="layer service" style="top:470px;"><span class="name">Reifenwechsel 39,95€</span><span class="detail">(Mit Reifenwäsche)</span></div>
  <div class="layer service" style="top:611px;"><span class="name">Smart-Repair ab 9,95€</span><span class="detail">(Kratzer und Schrammen, Dellen und Beulen)</span></div>
  <div class="layer service" style="top:750px;"><span class="name">KFZ-Inspektion ab 349,95€</span><span class="detail">(Großer Service &amp; Kleiner Service)</span></div>
  <div class="layer service" style="top:883px;"><span class="name">Fahrzeugpflege ab 23,95€</span><span class="detail">(Innen- &amp; Außenreinigung)</span></div>
  <div class="layer service" style="top:1013px;"><span class="name">Lackaufbereitung &amp; Politur</span></div>

  <h2 class="layer section-title steps-title">So funktioniert´s</h2>

  <div class="layer step" style="top:427px;"><span class="number">1.</span><span class="text">Gewünschten Termin,<br>Ort und Serviceoption wählen.</span></div>
  <div class="layer step" style="top:622px;"><span class="number">2.</span><span class="text">An gewähltem Datum und Abstellort parken,<br>Schlüssel mit erhaltenem<br>Pincode ins Schließfach geben.</span></div>
  <div class="layer step" style="top:862px;"><span class="number">3.</span><span class="text">Nach der Arbeit den Schlüssel aus<br>Schließfach holen und gewonnene<br>Freizeit genießen.</span></div>

  <div class="icon-slot" role="img" aria-label="Illustration: schwarze Limousine in Seitenansicht" style="left:374px; top:492px; width:110px; height:40px; background:#23252b;"></div>
  <div class="icon-slot" role="img" aria-label="Illustration: Tablet mit tippendem Finger" style="left:380px; top:700px; width:90px; height:62px; background:#2a2d35;"></div>
  <div class="icon-slot" role="img" aria-label="Illustration: Autoschlüssel" style="left:484px; top:706px; width:14px; height:56px; background:#2a2d35;"></div>
  <div class="icon-slot" role="img" aria-label="Illustration: glänzende schwarze Limousine mit Funkeln" style="left:374px; top:962px; width:104px; height:44px; background:#23252b;"></div>

  <div class="footer-logo"><span class="mark"></span><span>glanzamort</span></div>

  <span class="contact" style="left:330px; top:1112px;">info@glanzamort.de</span>
  <span class="contact" style="left:330px; top:1163px;">0176 20483917</span>
  <span class="contact" style="left:594px; top:1108px;">www.glanzamort.de</span>
  <span class="contact address" style="left:592px; top:1166px;">Lindenweg 14, 85057 Ingolstadt</span>
</div>
</body>
</html>
```